Wine Importer Needs a Wordpress Template

Our company, Corbanne Cellar Traders Ltd, requires a Wordpress template for our new website location (brastellcask.ie).

We specialise in importing Moldovan wine into Ireland. I have attached a presentation that has background information about the main winery and its wine. I would very much like to see something similar to this in feel and colour. I have also attached our logo which might be useful.

We are very much open to new ideas, so long as the result is something that is clean and easy to use.

Many thanks.
Updates

Project Deadline Extended
Reason: I have extended the deadline by a few days given that I was unable to respond timely to queries. My apologies to all for this. I will be available from now until the new deadline.

Project Deadline Extended

Industry/Entity Type

It Company

```html
<!DOCTYPE html>
<html lang="en">
<head>
<meta charset="utf-8">
<title>Corbanne Cellar Traders Ltd – Contact</title>
<link href="https://fonts.googleapis.com/css2?family=Lato:wght@300;400;700&display=swap" rel="stylesheet">
<style>
:root{
  --ink:#222;
  --text:#444;
  --muted:#777;
  --brand:#2e7d55;
  --accent:#f5576c;
  --rule:#c9c9dc;
  --field:#cfcfcf;
  --footer:#282828;
  --footer-bar:#4a4a4a;
  --footer-text:#e8e8e8;
  --footer-muted:#8a8a8a;
  --tile:#e55a1b;
}
*{box-sizing:border-box;margin:0;padding:0}
html,body{width:997px;height:1200px;overflow:hidden;background:#fff}
body{position:relative;font-family:'Lato',sans-serif;color:var(--text);font-size:11px}
.abs{position:absolute}

/* header */
.site-logo{left:162px;top:8px;width:100px;height:100px;border:2px solid var(--brand);border-radius:50%;
  display:flex;align-items:center;justify-content:center;text-align:center;color:var(--brand);
  font-weight:700;font-size:11px;line-height:1.3;padding:0 14px}
.main-nav a{position:absolute;top:23px;font-size:9.5px;font-weight:400;color:var(--ink);text-decoration:none;letter-spacing:.2px;white-space:nowrap}
.social{left:709px;top:21px;display:flex;gap:8px;align-items:center}
.social span{width:16px;height:16px;background:#111;display:block}
.social svg{display:block}

/* map */
.map{left:0;top:118px;width:997px;height:412px;
  background:linear-gradient(135deg,#dfe6d2 0%,#efe6cf 45%,#e4e8d8 70%,#cfdbe6 100%)}

/* contact */
.divider{left:168px;top:556px;width:654px;height:2px;background:var(--rule)}
.heading{font-size:10.5px;font-weight:700;color:var(--ink);letter-spacing:.2px}
.field{left:168px;width:314px;border:1px solid var(--field);padding:10px 10px;color:#aaa;font-size:10px;background:#fff}
.send-btn{left:168px;top:786px;width:132px;height:38px;background:var(--accent);color:#fff;font-weight:700;
  font-size:9.5px;display:flex;align-items:center;justify-content:center;letter-spacing:.3px}
.intro{left:508px;top:610px;width:314px;color:var(--muted);font-size:10px;line-height:17px}
.subhead{font-size:10px;font-weight:700;color:var(--ink)}
.rule-dark{left:508px;top:651px;width:314px;height:1px;background:#555}
.rule-accent{left:508px;top:734px;width:314px;height:1px;background:var(--accent)}
.info{left:508px;list-style:none;font-size:9.5px;color:var(--text)}
.info li{height:16.7px;display:flex;align-items:center;gap:7px}
.info svg{width:8px;height:8px;fill:#888;flex-shrink:0}

/* footer */
.footer{left:0;top:884px;width:997px;height:261px;background:var(--footer)}
.footer-bar{left:0;top:1145px;width:997px;height:55px;background:var(--footer-bar)}
.f-head{font-size:10.5px;font-weight:700;color:#bdbdbd;letter-spacing:.2px}
.f-text{font-size:9px;color:var(--footer-text);line-height:12px}
.tile{width:22px;height:22px;flex:0 0 22px;background:var(--tile);border:2px solid #444}
.link-item{left:182px;width:190px;display:flex;gap:7px;padding-bottom:6px;border-bottom:1px solid #3a3a3a}
.link-item p{font-size:8.5px;color:var(--footer-muted);line-height:12px}
.link-item b{color:var(--footer-text)}
.news{left:400px;width:190px;display:flex;gap:7px}
.news p{font-size:8.5px;color:var(--footer-text);line-height:11.5px}
.news small{display:block;color:var(--footer-muted);font-size:7.5px;margin-top:2px}
.tags{left:618px;top:1010px;width:180px;display:flex;flex-wrap:wrap;gap:3px}
.tags span{font-size:8px;color:var(--footer-text);border:1px solid #4a4a4a;padding:5px 5px;line-height:9px}
.foot-nav{left:182px;top:1162px;display:flex}
.foot-nav a{font-size:9.5px;color:#eee;text-decoration:none;margin-right:19px}
.rights{left:649px;top:1162px;font-size:9.5px;color:#eee}
</style>
</head>
<body>

<header>
  <div class="abs site-logo">Corbanne Cellar Traders Ltd</div>
  <nav class="main-nav">
    <a href="#" style="left:301px">HOME</a>
    <a href="#" style="left:352px">ABOUT</a>
    <a href="#" style="left:405px">PAGES</a>
    <a href="#" style="left:457px">PORTFOLIO</a>
    <a href="#" style="left:529px">BLOG</a>
    <a href="#" style="left:576px">FEATURES</a>
    <a href="#" style="left:643px">CONTACT</a>
  </nav>
  <div class="abs social">
    <span></span><span></span><span></span>
    <svg width="16" height="14" viewBox="0 0 16 14"><rect x="1" y="1" width="14" height="12" fill="none" stroke="#111" stroke-width="1.4"/><path d="M1 1l7 6 7-6" fill="none" stroke="#111" stroke-width="1.4"/></svg>
    <svg width="14" height="14" viewBox="0 0 24 24"><path fill="#111" d="M6.6 10.8a15.1 15.1 0 0 0 6.6 6.6l2.2-2.2c.3-.3.7-.4 1-.2 1.1.4 2.3.6 3.6.6.6 0 1 .4 1 1V20c0 .6-.4 1-1 1A17 17 0 0 1 3 4c0-.6.4-1 1-1h3.5c.6 0 1 .4 1 1 0 1.3.2 2.5.6 3.6.1.3 0 .7-.2 1z"/></svg>
  </div>
</header>

<div class="abs map" role="img" aria-label="Street map of Greater London with a location marker on central London"></div>

<main>
  <div class="abs divider"></div>

  <h2 class="abs heading" style="left:168px;top:587px">CONTACT FORM</h2>
  <div class="abs field" style="top:609px;height:34px">Name:</div>
  <div class="abs field" style="top:653px;height:34px">Email:</div>
  <div class="abs field" style="top:697px;height:81px">Message:</div>
  <div class="abs send-btn">SEND US A MESSAGE</div>

  <h2 class="abs heading" style="left:508px;top:587px">GET IN TOUCH</h2>
  <p class="abs intro">Lorem ipsum dolor sit amet, consectetur adipisicing elit. Soluta fuga esse laboriosam deleniti dolores</p>

  <div class="abs rule-dark"></div>
  <h3 class="abs subhead" style="left:508px;top:660px">Contact us</h3>
  <ul class="abs info" style="top:677px">
    <li><svg viewBox="0 0 10 10"><path d="M5 0a3.5 3.5 0 0 0-3.5 3.5C1.5 6 5 10 5 10s3.5-4 3.5-6.5A3.5 3.5 0 0 0 5 0zm0 5a1.4 1.4 0 1 1 0-2.8A1.4 1.4 0 0 1 5 5z"/></svg>Address: 1234 Street Name, City Name, United States</li>
    <li><svg viewBox="0 0 10 10"><rect x="1" y="1" width="8" height="8" rx="1"/></svg>Phone: (000) 000 000</li>
    <li><svg viewBox="0 0 10 10"><path d="M0 2h10v6H0z"/></svg>Email: email@email.com</li>
  </ul>

  <div class="abs rule-accent"></div>
  <h3 class="abs subhead" style="left:508px;top:743px">Bussines Hours</h3>
  <ul class="abs info" style="top:760px">
    <li><svg viewBox="0 0 10 10"><circle cx="5" cy="5" r="4" fill="none" stroke="#888" stroke-width="1.2"/><path d="M5 2.5V5h2" fill="none" stroke="#888"/></svg>Monday - Friday 9am to 5pm</li>
    <li><svg viewBox="0 0 10 10"><circle cx="5" cy="5" r="4" fill="none" stroke="#888" stroke-width="1.2"/><path d="M5 2.5V5h2" fill="none" stroke="#888"/></svg>Saturday - 9am to 2pm</li>
    <li><svg viewBox="0 0 10 10"><circle cx="5" cy="5" r="4" fill="none" stroke="#888" stroke-width="1.2"/><path d="M5 2.5V5h2" fill="none" stroke="#888"/></svg>Sunday - Closed</li>
  </ul>
</main>

<footer>
  <div class="abs footer"></div>

  <h4 class="abs f-head" style="left:182px;top:913px">LINK TO VISIT</h4>
  <p class="abs f-text" style="left:182px;top:939px;width:195px">Here are som einteresting stuff to visit, hope you will enjoy !</p>
  <div class="abs link-item" style="top:979px"><span class="tile"></span><p><b>Harlow Web Shop</b> - very fast shipping and top gear</p></div>
  <div class="abs link-item" style="top:1016px"><span class="tile"></span><p><b>Harlow Web Shop</b> - very fast shipping and top gear</p></div>
  <div class="abs link-item" style="top:1052px"><span class="tile"></span><p><b>Harlow Web Shop</b> - very fast shipping and top gear</p></div>
  <div class="abs link-item" style="top:1089px;border-bottom:0"><span class="tile"></span><p><b>Harlow Web Shop</b> - very fast shipping and top gear</p></div>

  <h4 class="abs f-head" style="left:400px;top:913px">LATEST NEWS</h4>
  <div class="abs news" style="top:940px"><span class="tile"></span><p>Lorem ipsum dolor sit amet, consectetur adipisicing elit. Inventore id quas voluptas commodi laborum facilis.<small>January 12, 2013 - 9:11 pm</small></p></div>
  <div class="abs news" style="top:999px"><span class="tile"></span><p>Lorem ipsum dolor sit amet, consectetur adipisicing elit. A, laborum quasi veniam iusto natus quibusdam voluptate beatae velit ex placeat.<small>January 12, 2013 - 9:11 pm</small></p></div>
  <div class="abs" style="left:400px;top:1061px;width:190px;border-top:1px dashed #555"></div>
  <div class="abs news" style="top:1070px"><span class="tile"></span><p>Ut adipiscing enim aliquam ut tristique phasellus. Et aliquet!<small>January 12, 2013 - 9:11 pm</small></p></div>

  <h4 class="abs f-head" style="left:618px;top:913px">BUSSINES HOURS</h4>
  <p class="abs f-text" style="left:618px;top:940px;color:var(--footer-muted)">Monday-Friday: <span style="color:var(--footer-text)">9am to 5pm</span><br>Saturday &amp; Sunday: <span style="color:var(--footer-text)">Closed</span></p>
  <h4 class="abs f-head" style="left:618px;top:988px">TAGS</h4>
  <div class="abs tags">
    <span>beautiful</span><span>design</span><span>love</span><span>we</span><span>inspiration</span><span>logo</span><span>print design</span><span>awesome</span><span>photography</span><span>logo design</span><span>branding</span>
  </div>

  <div class="abs footer-bar"></div>
  <nav class="abs foot-nav">
    <a href="#">Home</a><a href="#">About</a><a href="#">Pages</a><a href="#">Portfolio</a><a href="#">Blog</a><a href="#">Features</a><a href="#">Contact</a>
  </nav>
  <p class="abs rights">All Rights Reserved,</p>
</footer>

</body>
</html>
```